NZ First of it's kind solutions directory and marketplace for busy Mums needs a business card design

We need a business card design for our new nationwide business in NZ (long term plans to go global). We provide solutions to the everyday challenges that busy Mums face by connecting them with quality communities and suppliers of carefully selected, relevant products and services. We sell direct via our online marketplace. The final design should communicate our values of inclusivity, quality and smart solutions. Colours should incorporate our logo colour palette of #477077 and #6ba8b2. Our website is at https://www.brightnestly.com

Target Market(s)

busy Mums, Age 28 – 50, female, income over $100K, location main centres NZ primarily but NZ wide. Is likely juggling work or career with a young family. Probably had hobbies which have fallen by the wayside.
-Wants to succeed in her chosen career without compromising on family life
-to successfully juggle her career without feeling like she is compromising her children
- Is time poor, something always has to give and it’s generally her health (she’ll stay up late, get stressed)
- probably ex corporate or professional career. Has discretional income

Industry/Entity Type

Business

Contact Information for Business Card

Jodie Farnsworth, Founder, BrightNestly.com (Strapline Browse; Pick; Sorted), 48 Kowhai Terrace, Hillsborough, Auckland 1058, New Zealand. Mob: 021 437 518 Ph: +64 (0)9 584 7163

Font styles to use
Other font styles liked:
• Raleway, and/or Architects Daughter

Colors
00a990
33b8a4
86cfc6
cfeae6

Requirements
Must have
• the above details, streamline. the logo and colours associated with those logos
Should not have
• foil or metallic colours

```html
<!DOCTYPE html>
<html lang="en">
<head>
<meta charset="utf-8">
<title>BrightNestly business card</title>
<link rel="stylesheet" href="https://fonts.googleapis.com/css2?family=Raleway:wght@400;600;700&family=Open+Sans:wght@400;600&display=swap">
<style>
  :root {
    --teal-dark: #477077;
    --teal: #6ba8b2;
    --mint: #cfeae6;
    --mint-back: #d3ede9;
    --white: #ffffff;
    --ink: #2f3b3d;
    --bar-grey: #555859;
    --stage: #4a4a4a;
  }
  * { box-sizing: border-box; margin: 0; padding: 0; }
  html, body { width: 1100px; height: 1200px; overflow: hidden; }
  body { background: var(--stage); position: relative; font-family: "Open Sans", sans-serif; }

  .card {
    position: absolute; top: 452px; width: 493px; height: 296px; overflow: hidden;
    box-shadow: 0 6px 18px rgba(0,0,0,.35);
  }
  .card--front { left: 34px; background: var(--white); }
  .card--back { left: 573px; background: var(--mint-back); }

  .brand { position: absolute; display: flex; align-items: center; gap: 8px; }
  .brand__dot { width: 28px; height: 28px; border-radius: 50%; background: var(--teal-dark); }
  .brand__name {
    font-family: "Raleway", sans-serif; font-weight: 700; font-size: 27px;
    color: var(--teal-dark); letter-spacing: -0.3px;
  }
  .card--front .brand { left: 22px; top: 28px; }
  .card--back .brand { left: 0; right: 0; top: 106px; justify-content: center; }

  .band { position: absolute; left: 0; top: 127px; width: 100%; height: 169px; background: var(--teal-dark); }

  .identity { position: absolute; left: 0; top: 151px; width: 241px; height: 124px; background: var(--teal); }
  .identity__marker { position: absolute; left: 1px; top: 49px; width: 7px; height: 25px; background: var(--mint); }
  .identity__name {
    position: absolute; left: 24px; top: 47px; font-family: "Raleway", sans-serif;
    font-size: 16px; font-weight: 400; color: var(--white); letter-spacing: .6px;
  }
  .identity__name strong { font-weight: 600; }
  .identity__role {
    position: absolute; left: 24px; top: 69px; font-family: "Raleway", sans-serif;
    font-size: 8.5px; font-weight: 600; color: var(--white); letter-spacing: .5px;
  }

  .contact-row { position: absolute; left: 247px; width: 240px; height: 26px; }
  .contact-row__icon {
    position: absolute; left: 0; top: 0; width: 27px; height: 100%; background: var(--mint);
    display: flex; align-items: center; justify-content: center;
  }
  .contact-row__icon svg { width: 15px; height: 15px; fill: none; stroke: var(--teal-dark); stroke-width: 1.4; stroke-linecap: round; stroke-linejoin: round; }
  .contact-row__text {
    position: absolute; left: 31px; top: 0; right: 0; height: 100%; background: var(--mint);
    padding-left: 8px; display: flex; align-items: center;
    font-size: 10.5px; line-height: 1.05; color: var(--ink);
  }
  .row-mobile { top: 151px; }
  .row-phone { top: 183px; }
  .row-address { top: 214px; height: 28px; }
  .row-web { top: 247px; }

  .web-bar {
    position: absolute; left: 0; top: 258px; width: 100%; height: 19px; background: var(--bar-grey);
    color: var(--white); font-size: 10.5px; display: flex; align-items: center; justify-content: center;
  }
</style>
</head>
<body>

  <section class="card card--front" aria-label="Business card front">
    <div class="brand"><span class="brand__dot"></span><span class="brand__name">BrightNestly</span></div>
    <div class="band"></div>
    <div class="identity">
      <span class="identity__marker"></span>
      <p class="identity__name">JODIE <strong>FARNSWORTH</strong></p>
      <p class="identity__role">FOUNDER</p>
    </div>

    <div class="contact-row row-mobile">
      <span class="contact-row__icon"><svg viewBox="0 0 16 16"><rect x="4.5" y="1.5" width="7" height="13" rx="1"/><line x1="7" y1="12.5" x2="9" y2="12.5"/></svg></span>
      <span class="contact-row__text">021 437 518</span>
    </div>
    <div class="contact-row row-phone">
      <span class="contact-row__icon"><svg viewBox="0 0 16 16"><path d="M3 2.5l2.5-.5 1.3 3-1.5 1.2a8 8 0 0 0 4.5 4.5l1.2-1.5 3 1.3-.5 2.5C9 14 2 7 3 2.5z"/></svg></span>
      <span class="contact-row__text">+64 (0)9 584 7163</span>
    </div>
    <div class="contact-row row-address">
      <span class="contact-row__icon"><svg viewBox="0 0 16 16"><path d="M8 14.5s4.5-4.8 4.5-8a4.5 4.5 0 0 0-9 0c0 3.2 4.5 8 4.5 8z"/><circle cx="8" cy="6.5" r="1.6"/></svg></span>
      <span class="contact-row__text">48 Kowhai Terrace, Hillsborough,<br>Auckland 1058, New Zealand</span>
    </div>
    <div class="contact-row row-web">
      <span class="contact-row__icon"><svg viewBox="0 0 16 16"><circle cx="8" cy="8" r="6.3"/><ellipse cx="8" cy="8" rx="2.8" ry="6.3"/><line x1="1.7" y1="8" x2="14.3" y2="8"/></svg></span>
      <span class="contact-row__text">BrightNestly.com</span>
    </div>
  </section>

  <section class="card card--back" aria-label="Business card back">
    <div class="brand"><span class="brand__dot"></span><span class="brand__name">BrightNestly</span></div>
    <div class="web-bar">BrightNestly.com</div>
  </section>

</body>
</html>
```